Business Card for Managing Partner Investment Fund

To create a business card template for an investment fund manager. Business card should be more professional in nature, not too colorful, more upscale, and created using the attached logos and fund name files. I would prefer a black or gray color scheme, but am open to the use of color as well. I would prefer a double sided business card, but open to single sided business card designs as well. The business card should include: name, title, and contact information, as well as logo and company name. I would prefer a more stream-lined, simple business card design.
Updates
Address: 4190 NE 38th Ter. Ocala, FL 34470
Email: talvin47@quorimail.net
Phone: 561-347-9162
Title: managing partner
Name: Dorian Velsky
Fund Name: Ambergate Capital
Logos can be found in files attached to the brief
Target Market(s)
potential investors, other fund managers
Industry/Entity Type
Finance
Contact Information for Business Card
Name on card: Dorian Velsky
Title: Managing Partner
Colors
Designer to choose colors to be used in the design.
Requirements
Must have
- Phone number
- email address
- physical address
- title
- name
- logo
- Fund name
Nice to have
- simple layout
Should not have
- too many colors, busy fonts,

```html
<!DOCTYPE html>
<html lang="en">
<head>
<meta charset="UTF-8">
<title>Ambergate Capital — Business Card</title>
<link href="https://fonts.googleapis.com/css2?family=Cinzel:wght@500;600&family=Roboto:wght@400&family=Roboto+Condensed:wght@400;600&display=swap" rel="stylesheet">
<style>
  :root {
    --backdrop: #2b2b2b;
    --card-light: #f1f1f1;
    --card-dark: #5f5f5f;
    --ink: #555555;
    --ink-soft: #7a7a7a;
    --band-dark: #5a5a5a;
    --band-light: #8a8a8a;
    --divider: #b5b5b5;
    --white: #ffffff;
  }
  * { margin: 0; padding: 0; box-sizing: border-box; }
  html, body {
    width: 1200px; height: 960px; overflow: hidden;
    background: var(--backdrop);
  }
  .stage { position: relative; width: 1200px; height: 960px; }

  .card {
    position: absolute; width: 600px; height: 342px;
    box-shadow: 0 3px 8px rgba(0,0,0,0.45);
    overflow: hidden;
  }
  .card--front { left: 314px; top: 113px; background: var(--card-light); }
  .card--back  { left: 311px; top: 472px; background: var(--card-dark); }

  .brand {
    position: absolute; text-align: center;
    font-family: "Cinzel", serif; font-weight: 600;
    text-transform: uppercase; line-height: 1;
  }
  .card--front .brand { left: 36px; width: 260px; top: 176px; color: var(--ink); }
  .card--back .brand { left: 0; width: 600px; top: 178px; color: var(--white); }
  .brand__name { display: block; font-size: 36px; letter-spacing: 0.5px; }
  .brand__sub { display: block; font-size: 21px; letter-spacing: 3px; margin-top: 6px; }
  .card--back .brand__name { font-size: 43px; }
  .card--back .brand__sub { font-size: 24px; letter-spacing: 4px; margin-top: 7px; }

  .divider {
    position: absolute; left: 323px; top: 88px;
    width: 2px; height: 172px; background: var(--divider);
  }

  .contact {
    position: absolute; left: 356px; top: 91px;
    font-family: "Roboto", sans-serif; color: var(--ink);
  }
  .contact__name {
    font-family: "Roboto Condensed", sans-serif; font-weight: 600;
    font-size: 21px; text-transform: uppercase; color: var(--ink);
    line-height: 1.1;
  }
  .contact__title {
    font-family: "Roboto Condensed", sans-serif; font-weight: 400;
    font-size: 16px; text-transform: uppercase; color: var(--ink-soft);
    margin-top: 2px;
  }
  .contact__address { font-size: 14px; line-height: 18px; margin-top: 14px; }
  .contact__list { list-style: none; margin-top: 11px; }
  .contact__item {
    display: flex; align-items: center; gap: 9px;
    font-size: 14px; line-height: 19.5px;
  }
  .contact__icon { width: 13px; height: 13px; fill: var(--ink); flex: none; }

  .band { position: absolute; left: 0; bottom: 0; width: 600px; height: 22px; }

  .card--back .web {
    position: absolute; left: 0; width: 600px; top: 286px;
    text-align: center; font-family: "Roboto", sans-serif;
    font-size: 14px; letter-spacing: 4px; color: var(--white);
  }
</style>
</head>
<body>
<main class="stage">
  <section class="card card--front" aria-label="Card front">
    <div class="brand">
      <span class="brand__name">Ambergate</span>
      <span class="brand__sub">Capital</span>
    </div>
    <div class="divider"></div>
    <div class="contact">
      <p class="contact__name">Dorian Velsky</p>
      <p class="contact__title">Managing Partner</p>
      <p class="contact__address">1200 Sample Avenue<br>Anytown, FL 00000</p>
      <ul class="contact__list">
        <li class="contact__item">
          <svg class="contact__icon" viewBox="0 0 24 24"><path d="M6.6 10.8a15.1 15.1 0 0 0 6.6 6.6l2.2-2.2a1 1 0 0 1 1-.25 11.4 11.4 0 0 0 3.6.57 1 1 0 0 1 1 1V20a1 1 0 0 1-1 1A17 17 0 0 1 3 4a1 1 0 0 1 1-1h3.5a1 1 0 0 1 1 1c0 1.25.2 2.45.57 3.57a1 1 0 0 1-.25 1z"/></svg>
          555-010-0000
        </li>
        <li class="contact__item">
          <svg class="contact__icon" viewBox="0 0 24 24"><path d="M2 5h20v14H2z M2 5l10 8 10-8" fill="none" stroke="#555" stroke-width="2"/><path d="M3 6l9 7 9-7v12H3z"/></svg>
          dorian@ambergatefund.net
        </li>
        <li class="contact__item">
          <svg class="contact__icon" viewBox="0 0 24 24"><circle cx="12" cy="12" r="10"/><path d="M2 12h20M12 2c3 3 3 17 0 20M12 2c-3 3-3 17 0 20" fill="none" stroke="#f1f1f1" stroke-width="1.6"/></svg>
          www.ambergatefund.net
        </li>
      </ul>
    </div>
    <svg class="band" viewBox="0 0 600 22" preserveAspectRatio="none">
      <rect x="0" y="0" width="600" height="22" fill="var(--band-dark)"/>
      <polygon points="394,0 600,0 600,22 389,22" fill="var(--band-light)"/>
      <polygon points="391,0 394,0 389,22 386,22" fill="var(--white)"/>
    </svg>
  </section>

  <section class="card card--back" aria-label="Card back">
    <div class="brand">
      <span class="brand__name">Ambergate</span>
      <span class="brand__sub">Capital</span>
    </div>
    <p class="web">www.ambergatefund.net</p>
  </section>
</main>
</body>
</html>
```